Webdesign für lokalen Dart-Shop
Zielgruppe
Wir sind ein lokaler Dart-Shop in Hamburg, welcher in Norddeutschland sehr beliebt ist und bundesweit das Größte Angebot bietet. Durch unseren Online-Shop möchte wir unseren Radius erweitern.
Zielgruppe: Dart Anfänger, Fortgeschrittene sowie Vereine und Unternehmen
Aufgabenstellung
In jedem Fall das Haupt-Element unseres Logo´s, einer Dart-Scheibe.

```html
<!DOCTYPE html>
<html lang="de">
<head>
<meta charset="utf-8">
<title>Pfeilwerk Nord – Menü</title>
<link rel="stylesheet" href="https://fonts.googleapis.com/css2?family=Montserrat:wght@400;500;600;700&display=swap">
<style>
  :root {
    --white: #ffffff;
    --ink: #111111;
    --ink-soft: #1c1c1c;
    --hero-text: #b9b6b4;
    --hero-button: #9c9a99;
    --notice-bg: #8e8e8e;
    --brick-dark: #3a2723;
    --brick-mid: #5a3a33;
    --shadow: rgba(0,0,0,0.08);
  }
  * { margin: 0; padding: 0; box-sizing: border-box; }
  html, body { width: 1200px; height: 2598px; overflow: hidden; }
  body { font-family: "Montserrat", Arial, sans-serif; background: var(--white); color: var(--ink); position: relative; }

  .site-header { position: absolute; left: 0; top: 0; width: 1200px; height: 1206px; background: var(--white); }
  .brand { position: absolute; left: 70px; top: 150px; display: flex; align-items: center; gap: 22px; }
  .brand-dot { width: 84px; height: 84px; border-radius: 50%; background: var(--ink); }
  .brand-name { font-weight: 700; font-size: 40px; line-height: 1.05; color: var(--ink); width: 220px; }

  .header-icon { position: absolute; top: 155px; width: 80px; height: 80px; }
  .icon-search { left: 642px; }
  .icon-user { left: 843px; }
  .icon-close { left: 1041px; top: 142px; width: 120px; height: 120px; border-radius: 50%; box-shadow: 0 6px 30px var(--shadow); display: flex; align-items: center; justify-content: center; }

  .main-nav { position: absolute; left: 70px; top: 430px; }
  .main-nav a { display: block; color: var(--ink-soft); text-decoration: none; font-size: 48px; font-weight: 500; height: 128px; line-height: 1; }
  .main-nav a.current { font-size: 58px; font-weight: 700; height: 135px; }

  .hero { position: absolute; left: 0; top: 1206px; width: 1200px; height: 756px;
          background: linear-gradient(180deg, #2b2a2c 0%, var(--brick-dark) 35%, var(--brick-mid) 70%, #4a302b 100%); }
  .hero-shade { position: absolute; inset: 0; background: rgba(0,0,0,0.35); }
  .hero-title { position: absolute; left: 70px; top: 1440px; font-size: 61px; font-weight: 700; line-height: 77px; color: var(--hero-text); }
  .hero-button { position: absolute; left: 70px; top: 1664px; width: 576px; height: 157px; border-radius: 79px; background: var(--hero-button);
                 display: flex; align-items: center; justify-content: center; font-size: 41px; font-weight: 700; color: var(--ink); }

  .notice { position: absolute; left: 0; top: 1962px; width: 1200px; height: 636px; background: var(--notice-bg); }
  .notice-text { position: absolute; left: 70px; top: 2092px; font-size: 48px; font-weight: 700; line-height: 61px; color: var(--ink); }
  .notice-button { position: absolute; left: 70px; top: 2288px; width: 503px; height: 157px; border-radius: 79px; border: 4px solid var(--ink);
                   display: flex; align-items: center; justify-content: center; font-size: 41px; font-weight: 700; color: var(--ink); }
</style>
</head>
<body>
  <header class="site-header">
    <div class="brand">
      <span class="brand-dot"></span>
      <span class="brand-name">Pfeilwerk Nord</span>
    </div>
    <svg class="header-icon icon-search" viewBox="0 0 80 80" fill="none" stroke="#111" stroke-width="6">
      <circle cx="36" cy="36" r="28"/><line x1="57" y1="57" x2="74" y2="74" stroke-linecap="round"/>
    </svg>
    <svg class="header-icon icon-user" viewBox="0 0 80 80" fill="none" stroke="#111" stroke-width="6">
      <circle cx="40" cy="22" r="17"/><path d="M8 76 C10 52 24 44 40 44 C56 44 70 52 72 76"/>
    </svg>
    <div class="icon-close">
      <svg width="62" height="62" viewBox="0 0 62 62" stroke="#111" stroke-width="6" stroke-linecap="round">
        <line x1="4" y1="4" x2="58" y2="58"/><line x1="58" y1="4" x2="4" y2="58"/>
      </svg>
    </div>
    <nav class="main-nav">
      <a class="current" href="#">Start</a>
      <a href="#">Aktuelles</a>
      <a href="#">Über uns</a>
      <a href="#">Kontakt</a>
      <a href="#">Online Shop</a>
    </nav>
  </header>

  <section class="hero" role="img" aria-label="Foto: Schaufenster des Dart-Shops mit Leuchtreklame vor einer Backsteinfassade">
    <div class="hero-shade"></div>
  </section>
  <h1 class="hero-title">Lorem ipsum<br>dolor sit amet.</h1>
  <div class="hero-button">Zum Online-Shop</div>

  <section class="notice"></section>
  <p class="notice-text">Aufgrund der Corona-Pandemie ist<br>unser Shop derzeit geschlossen.</p>
  <div class="notice-button">Corona-Info</div>
</body>
</html>
```